Keystone Ridge Construction LLC

We need a professional and colorful website that describes our company [please see below]:

CORE COMPETENCIES

About Us: Keystone Ridge Construction, LLC is a veteran-owned business, and is a leading force in the construction industry. We have continuously provided exceptional services to our clients. With a wealth of experience and a commitment of excellence, we have earned a reputation for delivering high-quality projects on time and within budget.

Core Competencies:

Experience: With decades of experience, we bring unparalleled expertise to every project we undertake. Our team consists of seasoned professionals who are experts in their respective fields.

Portfolio: Our portfolio encompasses a wide range of construction projects, including commercial building, industrial facilities, infrastructure development and more.

Innovation: We stay at the forefront of industry trends and technologies, leveraging the latest tools and techniques to deliver innovative solutions.

Client Satisfaction: Our commitment to client satisfaction is unwavering. We prioritize open communication, transparency, and responsiveness, working closely with clients to understand their needs and deliver results.

Safety: Safety is our top priority on every job site. We adhere to the highest safety standards and implement rigorous safety protocols to ensure the well-being of our workers and stakeholders.

KEY SERVICES

General Contracting
Construction Management
Design-Build Services
Pre-construction Planning
Value Engineering
Sustainable Construction Practices
Renovation and Remodeling
Quality Assurance and Control
Project Estimating and Budgeting
Permitting and Regulatory Compliance

CONTACT INFORMATION

Douglas Whitfield, President
Email Address [TBD]
Website Address [TBD]
555.214.6093

Federal Government and Commercial Agencies

Construction and Design Build

• Please use our attached logo and color scheme that was designed through Pixel Forum. Please include the Nation's Capitol building with a patriotic feel and include a diverse work force. Include federal buildings in the pictures. Please include in the opeing tagline that the company is Veteran Owned.

```html
<!DOCTYPE html>
<html lang="en">
<head>
<meta charset="utf-8">
<title>Keystone Ridge Construction, LLC</title>
<link rel="stylesheet" href="https://fonts.googleapis.com/css2?family=Merriweather:wght@700;900&family=Montserrat:wght@400;500;600;700&display=swap">
<style>
:root{
  --navy:#2a3170;
  --navy-dark:#222961;
  --green:#8cc63f;
  --paper:#f3f3ee;
  --line:#cfcfcf;
  --ink:#1f1f2e;
  --muted:#5a5a66;
  --white:#ffffff;
}
*{box-sizing:border-box;margin:0;padding:0}
html,body{width:1200px;height:3807px;overflow:hidden}
body{position:relative;font-family:'Montserrat',sans-serif;color:var(--ink);background:var(--white)}
.abs{position:absolute}
.serif{font-family:'Merriweather',serif;font-weight:900}

/* header */
.site-header{left:0;top:0;width:1200px;height:93px;background:var(--white)}
.brand{display:flex;align-items:center;gap:8px;font-weight:700;color:var(--navy);font-size:15px;letter-spacing:.5px;white-space:nowrap}
.brand-mark{width:14px;height:14px;background:var(--navy)}
.header-brand{left:140px;top:36px}
.nav{top:36px;font-size:14px;font-weight:500;color:var(--ink)}
.btn-green{background:var(--green);color:var(--white);font-size:13px;font-weight:500;display:flex;align-items:center;justify-content:center;gap:8px}
.nav-cta{left:930px;top:27px;width:130px;height:37px}
.header-rule{left:572px;top:88px;width:628px;height:5px;background:var(--green)}

/* hero */
.hero{left:0;top:93px;width:1200px;height:516px;background:linear-gradient(180deg,#4a4f7a 0%,#8a6a86 35%,#c88a6a 55%,#3a4266 78%,#23294d 100%)}
.hero-shade{left:0;top:93px;width:1200px;height:516px;background:linear-gradient(90deg,rgba(25,28,60,.55),rgba(25,28,60,.15))}
.hero-title{left:140px;top:216px;width:820px;color:var(--white);font-size:36px;line-height:51px;text-transform:uppercase}
.hero-sub{left:140px;top:385px;color:var(--white);font-size:15px;font-weight:500;letter-spacing:.2px;white-space:nowrap}
.btn-white{background:var(--white);color:var(--ink);font-size:14px;font-weight:600;display:flex;align-items:center;justify-content:center;gap:8px;white-space:nowrap}
.hero-btn1{left:140px;top:440px;width:232px;height:45px}
.hero-btn2{left:387px;top:440px;width:145px;height:45px;font-size:14px}
.scroll{left:540px;top:543px;width:120px;text-align:center;color:var(--white);font-size:10px;font-weight:500}
.side-rail{left:39px;top:215px;width:1px;height:272px;background:rgba(255,255,255,.7)}
.side-dot{left:36px;width:7px;height:7px;border-radius:50%;background:var(--white)}

/* services */
.services-panel{left:143px;top:884px;width:804px;height:390px;background:var(--paper)}
.services-panel2{left:811px;top:1385px;width:136px;height:118px;background:var(--paper)}
.services-heading{left:192px;top:988px;font-size:31px;color:var(--navy)}
.services-intro{left:192px;top:1036px;width:330px;font-size:13px;line-height:23px;color:var(--ink)}
.svc{width:249px;height:228px;border:1px solid var(--line);background:var(--white);padding:30px 22px 0 24px}
.svc svg{width:46px;height:46px;display:block}
.svc h3{margin-top:22px;font-size:14px;font-weight:600;color:var(--ink);white-space:nowrap;letter-spacing:-.1px}
.svc p{margin-top:12px;font-size:11px;line-height:19px;color:var(--muted)}
.svc.active{background:var(--navy)}
.svc.active h3,.svc.active p{color:var(--white)}
.crane{left:22px;top:1485px;width:241px;height:318px;background:linear-gradient(180deg,#f7d2ae 0%,#f3dcc6 60%,#eceef0 100%)}

/* about */
.about-band{left:0;top:1803px;width:1200px;height:1023px;background:var(--navy)}
.capitol{left:260px;top:1712px;width:940px;height:368px;background:linear-gradient(100deg,#9bc54a 0%,#b9d67a 30%,#e7ecef 55%,#cfd6d9 75%,#4d6a3a 100%)}
.about-title{left:328px;top:1993px;font-size:34px;color:var(--white)}
.video{left:242px;top:2124px;width:320px;height:177px;background:linear-gradient(135deg,#b8cbe0,#5c7896 50%,#2b3f5c)}
.play{left:382px;top:2192px;width:40px;height:40px;border-radius:50%;background:var(--white)}
.about-card{left:600px;top:1948px;width:368px;height:353px;background:var(--white);padding:42px 30px 0}
.about-card h2{font-size:15px;font-weight:700;color:var(--navy);letter-spacing:.3px}
.about-card h2 span{color:var(--green)}
.about-card p{margin-top:14px;font-size:13.5px;line-height:24px;color:var(--ink)}

/* why choose us */
.why-heading{left:143px;top:2400px;font-size:30px;color:var(--white)}
.why-intro{left:439px;top:2397px;width:630px;font-size:12.5px;line-height:23px;color:var(--white)}
.why-link{top:2537px;height:0;border-top:2px dashed var(--green)}
.why-item{top:2498px;width:186px;text-align:center;color:var(--white)}
.why-icon{width:80px;height:80px;border-radius:50%;background:var(--white);margin:0 auto;display:flex;align-items:center;justify-content:center}
.why-item h3{margin-top:28px;font-size:16px;font-weight:600;white-space:nowrap}
.why-item p{margin-top:8px;font-size:10.5px;line-height:19px}

/* testimonials */
.testi-heading{left:0;top:2896px;width:1200px;text-align:center;font-size:31px;color:var(--navy)}
.quote{background:var(--paper)}
.quote-main{left:303px;top:2978px;width:593px;height:241px;padding:40px 25px 0;text-align:center}
.quote-side-l{left:0;top:2978px;width:272px;height:241px;background:var(--white);box-shadow:0 0 14px rgba(0,0,0,.08);overflow:hidden}
.quote-side-r{left:927px;top:2978px;width:273px;height:241px;background:var(--white);box-shadow:0 0 14px rgba(0,0,0,.08);overflow:hidden}
.qmark{font-family:'Merriweather',serif;font-weight:900;font-size:110px;line-height:1;color:var(--green)}
.quote-text{font-size:13.5px;line-height:23px;color:var(--ink)}
.stars{color:#f5a623;font-size:16px;letter-spacing:3px;margin-top:12px}
.who{font-size:16px;font-weight:600;margin-top:6px}
.role{font-size:12px;color:var(--green);margin-top:4px;white-space:nowrap}
.dots{left:566px;top:3260px;display:flex;gap:13px}
.dots i{width:9px;height:9px;border-radius:50%;background:#9aa0c4;display:block}
.dots i:first-child{background:var(--green)}

/* cta */
.cta-green{left:0;top:3374px;width:1200px;height:154px;background:var(--green)}
.cta-photo{left:0;top:3355px;width:305px;height:173px;background:linear-gradient(135deg,#6b7e99,#2f3d5a 60%,#1d2640);clip-path:polygon(0 0,100% 0,74% 100%,0 100%)}
.cta-text{left:368px;top:3430px;font-size:30px;color:var(--white);white-space:nowrap}
.cta-btn{left:930px;top:3432px;width:130px;height:37px;font-size:13px;font-weight:600}

/* footer */
.footer{left:0;top:3528px;width:1200px;height:233px;background:var(--navy)}
.footer-shape{left:980px;top:3540px;width:160px;height:221px;background:rgba(255,255,255,.05)}
.footer-brand{left:143px;top:3665px;color:var(--white)}
.footer-brand .brand-mark{background:var(--white)}
.footer-divider{left:338px;top:3628px;width:1px;height:77px;background:rgba(255,255,255,.6)}
.footer-about{left:367px;top:3624px;width:350px;font-size:13px;line-height:23px;color:var(--white)}
.follow{left:789px;top:3643px;font-size:15px;font-weight:600;color:var(--white);border-bottom:2px solid var(--green);padding-bottom:2px}
.social{top:3638px;width:32px;height:32px;border-radius:50%;background:var(--white)}
.social.on{background:var(--green)}
.bottom-bar{left:0;top:3761px;width:1200px;height:46px;background:var(--navy-dark)}
.copy{left:140px;top:3777px;color:var(--white);font-size:12px}
.legal{left:831px;top:3777px;display:flex;gap:16px;color:var(--white);font-size:12px}
.legal span+span{border-left:1px solid rgba(255,255,255,.7);padding-left:16px}
</style>
</head>
<body>

<header>
  <div class="abs site-header"></div>
  <div class="abs brand header-brand"><span class="brand-mark"></span>KEYSTONE RIDGE</div>
  <nav>
    <span class="abs nav" style="left:580px">Home</span>
    <span class="abs nav" style="left:654px">About Us</span>
    <span class="abs nav" style="left:747px">Services</span>
    <span class="abs nav" style="left:836px">Portfolio</span>
    <span class="abs btn-green nav-cta">Contact Us</span>
  </nav>
  <div class="abs header-rule"></div>
</header>

<section>
  <div class="abs hero" role="img" aria-label="Construction cranes over a city skyline at sunset"></div>
  <div class="abs hero-shade"></div>
  <div class="abs side-rail"></div>
  <span class="abs side-dot" style="top:292px" aria-label="Social link"></span>
  <span class="abs side-dot" style="top:348px" aria-label="Social link"></span>
  <span class="abs side-dot" style="top:403px" aria-label="Social link"></span>
  <h1 class="abs hero-title serif">Keystone Ridge Construction, LLC - Leading Construction Management Services</h1>
  <p class="abs hero-sub">DELIVERING EXCEPTIONAL RESULTS FOR FEDERAL AND COMMERCIAL AGENCIES</p>
  <a class="abs btn-white hero-btn1">Explore Our Services
    <svg width="16" height="12" viewBox="0 0 16 12"><path d="M0 6h14M9 1l5 5-5 5" stroke="#1f1f2e" stroke-width="1.6" fill="none"/></svg></a>
  <a class="abs btn-green hero-btn2">Contact Us
    <svg width="16" height="12" viewBox="0 0 16 12"><path d="M0 6h14M9 1l5 5-5 5" stroke="#fff" stroke-width="1.6" fill="none"/></svg></a>
  <div class="abs scroll">SCROLL DOWN<br>
    <svg width="10" height="8" viewBox="0 0 10 8"><path d="M1 2l4 4 4-4" stroke="#fff" stroke-width="1.4" fill="none"/></svg></div>
</section>

<section>
  <div class="abs services-panel"></div>
  <div class="abs services-panel2"></div>
  <h2 class="abs services-heading serif">Our Services</h2>
  <p class="abs services-intro">At Keystone Ridge Construction, LLC, we offer a comprehensive range of services to meet all your construction needs:</p>

  <div class="abs svc" style="left:315px;top:702px">
    <svg viewBox="0 0 46 46" fill="none" stroke="#2a3170" stroke-width="1.5"><rect x="4" y="20" width="14" height="22"/><rect x="20" y="10" width="12" height="32"/><path d="M32 4h10M36 4v16M8 26h6M8 32h6M24 16h4M24 22h4M24 28h4"/></svg>
    <h3>General Contracting</h3>
    <p>We manage and oversee construction projects from start to finish, ensuring timely completion and adherence to specifications.</p>
  </div>
  <div class="abs svc" style="left:563px;top:702px">
    <svg viewBox="0 0 46 46" fill="none" stroke="#2a3170" stroke-width="1.5"><circle cx="23" cy="14" r="7"/><circle cx="23" cy="14" r="2.5"/><path d="M8 32l8 8M30 40l8-8M12 30h22M16 36h14"/></svg>
    <h3>Construction Management</h3>
    <p>Our team coordinates all aspects of your construction project, from planning through execution, to ensure efficiency and effectiveness.</p>
  </div>
  <div class="abs svc" style="left:811px;top:702px">
    <svg viewBox="0 0 46 46" fill="none" stroke="#2a3170" stroke-width="1.5"><rect x="6" y="12" width="34" height="26" transform="rotate(-30 23 25)"/><path d="M12 8l26 30M36 6l-24 30"/></svg>
    <h3>Design Build Services</h3>
    <p>We offer an integrated approach where design and construction services are combined, streamlining the process and improving project outcomes.</p>
  </div>
  <div class="abs svc" style="left:563px;top:930px">
    <svg viewBox="0 0 46 46" fill="none" stroke="#2a3170" stroke-width="1.5"><circle cx="18" cy="23" r="13"/><circle cx="18" cy="23" r="5"/><path d="M31 14h8M31 23h10M31 32h8"/><circle cx="40" cy="14" r="2"/><circle cx="42" cy="32" r="2"/></svg>
    <h3>Pre Construction Planning</h3>
    <p>We assist in the initial stages of your project, including feasibility studies, budgeting, and scheduling, to ensure a smooth start.</p>
  </div>
  <div class="abs svc" style="left:811px;top:930px">
    <svg viewBox="0 0 46 46" fill="none" stroke="#2a3170" stroke-width="1.5"><circle cx="23" cy="20" r="12"/><circle cx="23" cy="20" r="5"/><path d="M10 38h26M14 32l-4 6M32 32l4 6"/></svg>
    <h3>Value Engineering</h3>
    <p>We analyze project functions and costs to optimize value, reducing expenses without compromising quality or performance.</p>
  </div>
  <div class="abs svc" style="left:315px;top:1157px">
    <svg viewBox="0 0 46 46" fill="none" stroke="#2a3170" stroke-width="1.5"><circle cx="23" cy="23" r="17"/><path d="M23 32V18M23 22c-6 0-8-4-8-7 5 0 8 2 8 7zM23 22c6 0 8-4 8-7-5 0-8 2-8 7z"/></svg>
    <h3>Sustainable Construction</h3>
    <p>We incorporate eco-friendly practices and materials to minimize environmental impact and promote sustainability in every project.</p>
  </div>
  <div class="abs svc active" style="left:563px;top:1157px">
    <svg viewBox="0 0 46 46" fill="none" stroke="#8cc63f" stroke-width="1.5"><path d="M4 22L20 8l16 14M8 19v20h24V19"/><rect x="16" y="27" width="8" height="12"/><path d="M34 24v14M30 24h8"/></svg>
    <h3>Renovation &amp; Remodeling</h3>
    <p>We provide expert services to update and enhance existing structures, improving functionality and aesthetics.</p>
  </div>
  <div class="abs svc" style="left:811px;top:1157px">
    <svg viewBox="0 0 46 46" fill="none" stroke="#2a3170" stroke-width="1.5"><circle cx="23" cy="18" r="13"/><path d="M17 18l4 4 8-8M16 29l-4 13 6-3 4 4 1-10M30 29l4 13-6-3-4 4"/></svg>
    <h3 style="font-size:13.5px">Quality Assurance &amp; Control</h3>
    <p>Our rigorous QA/QC processes ensure that all work meets the highest standards and adheres to project specifications.</p>
  </div>
  <div class="abs svc" style="left:315px;top:1385px">
    <svg viewBox="0 0 46 46" fill="none" stroke="#2a3170" stroke-width="1.5"><rect x="6" y="4" width="26" height="36"/><circle cx="14" cy="13" r="5"/><path d="M22 12h6M12 24h16M12 30h12M40 14L26 36l-2 5 5-3 14-22z"/></svg>
    <h3>Project Estimating &amp; Budget</h3>
    <p>We offer detailed cost estimates and budgeting services to help you plan and manage your project finances effectively.</p>
  </div>
  <div class="abs svc" style="left:563px;top:1385px">
    <svg viewBox="0 0 46 46" fill="none" stroke="#2a3170" stroke-width="1.5"><rect x="6" y="4" width="24" height="34"/><path d="M11 12h14M11 18h14M11 24h10"/><circle cx="32" cy="32" r="8"/><path d="M28 32l3 3 5-6"/></svg>
    <h3>Permitting Compliance</h3>
    <p>We handle all aspects of obtaining necessary permits and ensuring compliance with local regulations and building codes.</p>
  </div>

  <div class="abs crane" role="img" aria-label="Orange tower crane illustration"></div>
</section>

<section>
  <div class="abs about-band"></div>
  <div class="abs capitol" role="img" aria-label="Nation's Capitol building under a green-tinted sky"></div>
  <svg class="abs" style="left:282px;top:1728px" width="70" height="230" viewBox="0 0 70 230" fill="none" stroke="#fff" stroke-width="1.5"><path d="M2 0v225l66-60V20"/></svg>
  <h2 class="abs about-title serif">About Us</h2>
  <div class="abs video" role="img" aria-label="Glass office towers viewed from below"></div>
  <div class="abs play"></div>
  <svg class="abs" style="left:397px;top:2205px" width="12" height="14" viewBox="0 0 12 14"><path d="M0 0l12 7-12 7z" fill="#1f1f2e"/></svg>
  <div class="abs about-card">
    <h2>WE ARE <span>CONSTRUCTION EXPERTS</span></h2>
    <p>Keystone Ridge Construction, LLC is a proud veteran-owned enterprise and a distinguished leader in the construction sector. Over the years, we have steadfastly delivered exceptional services to a diverse clientele, earning their trust and satisfaction. Our team boasts a wealth of experience across various facets of construction, allowing us to tackle projects of any scale and complexity with confidence &amp; precision.</p>
  </div>

  <h2 class="abs why-heading serif">Why Choose Us</h2>
  <p class="abs why-intro">We offer unparalleled expertise, delivering customized solutions that meet your unique needs. Our commitment to quality and transparent communication ensures you receive exceptional results.</p>

  <div class="abs why-link" style="left:248px;width:110px"></div>
  <div class="abs why-link" style="left:446px;width:110px"></div>
  <div class="abs why-link" style="left:644px;width:110px"></div>
  <div class="abs why-link" style="left:842px;width:110px"></div>

  <div class="abs why-item" style="left:111px">
    <div class="why-icon"><svg width="40" height="40" viewBox="0 0 40 40" fill="none" stroke="#2a3170" stroke-width="1.5"><path d="M6 18h6v16H6zM12 20l6-10c3 0 3 3 2 6h8c2 0 3 2 2 4l-3 10c-1 2-2 3-4 3H12"/><path d="M30 4l1.5 3 3 .5-2.2 2 .6 3-2.9-1.5-2.9 1.5.6-3-2.2-2 3-.5z" stroke="#8cc63f"/></svg></div>
    <h3>Experience</h3>
    <p>With decades of experience, we bring unparalleled expe-rtise to every project we undertake. Our team consist of seasoned professionals who are experts in their respective fields</p>
  </div>
  <div class="abs why-item" style="left:309px">
    <div class="why-icon"><svg width="40" height="40" viewBox="0 0 40 40" fill="none" stroke="#2a3170" stroke-width="1.5"><rect x="14" y="5" width="18" height="26"/><rect x="8" y="12" width="16" height="22" fill="#fff"/><path d="M12 20h8M12 25h8M12 30h5"/></svg></div>
    <h3>Portfolio</h3>
    <p>Our portfolio encompasses a wide range of construction projects, including commercial building, industrial facilities, infrastructure development and more</p>
  </div>
  <div class="abs why-item" style="left:507px">
    <div class="why-icon"><svg width="40" height="40" viewBox="0 0 40 40" fill="none" stroke="#2a3170" stroke-width="1.5"><circle cx="20" cy="17" r="8"/><path d="M16 25v6h8v-6M17 35h6M20 3v3M8 7l2 2M32 7l-2 2M4 17h3M33 17h3"/><circle cx="20" cy="17" r="3" stroke="#8cc63f"/></svg></div>
    <h3>Innovation</h3>
    <p>We stay at the forefront of industry trends and technologies, leveraging the latest tools and techniques to deliver innovative solutions</p>
  </div>
  <div class="abs why-item" style="left:705px">
    <div class="why-icon"><svg width="40" height="40" viewBox="0 0 40 40" fill="none" stroke="#2a3170" stroke-width="1.5"><circle cx="20" cy="12" r="5"/><path d="M11 26c0-5 4-8 9-8s9 3 9 8"/><path d="M4 28c6 0 8 4 16 4s10-4 16-4" stroke="#8cc63f"/></svg></div>
    <h3>Client Satisfaction</h3>
    <p>Our commitment to client satisfaction is unwavering. We prioritize open communica-tion, transparency, &amp; responsi-veness, working clo-sely with clients to understa-nd their needs &amp; deliver results</p>
  </div>
  <div class="abs why-item" style="left:902px">
    <div class="why-icon"><svg width="40" height="40" viewBox="0 0 40 40" fill="none" stroke="#2a3170" stroke-width="1.5"><path d="M20 4l13 5v10c0 9-6 14-13 17C13 33 7 28 7 19V9z"/><path d="M14 20l4 4 8-8" stroke="#8cc63f"/></svg></div>
    <h3>Safety</h3>
    <p>Safety is our top priority on every job site. We adhere to the highest safety standards and implement rigorous safety protocols to ensure the well-being of our workers and stakeholders</p>
  </div>
</section>

<section>
  <h2 class="abs testi-heading serif">What Say Our Clients</h2>

  <div class="abs quote-side-l">
    <div class="quote-text" style="position:absolute;left:-320px;top:40px;width:580px;text-align:center">Lorem Ipsum Is Simply Dummy Text Of The Printing And Typesetting Industry. Lorem Ipsum Has Been The Industry's Standard Dummy Text Ever Since The 1500s, When An Unknown Printer Took A Galley Of Type And Scrambled It To Make A Type Specimen Book. It Has Survived Not Only Five Centuries.</div>
    <div class="stars" style="position:absolute;left:-10px;top:152px">★★</div>
    <div class="role" style="position:absolute;left:-20px;top:198px;color:var(--ink)">Heritage Books</div>
  </div>
  <div class="abs quote-side-r">
    <div class="qmark" style="position:absolute;left:58px;top:-22px">”</div>
    <div class="quote-text" style="position:absolute;left:20px;top:40px;width:580px;text-align:left;padding-left:25px">Lorem Ipsum Is Simply Dummy Text Of The Printing And Typesetting Industry. Lorem Ipsum Has Been The Industry's Standard Dummy Text Ever Since The 1500s, When An Unknown Printer Took A Galley Of Type And Scrambled It To Make A Type Specimen Book. It Has Survived Not Only Five Centuries.</div>
    <div class="stars" style="position:absolute;left:250px;top:152px">★★</div>
    <div class="role" style="position:absolute;left:225px;top:198px;color:var(--ink)">Author Of Heritage Books</div>
  </div>
  <div class="abs quote quote-main">
    <div class="qmark" style="position:absolute;left:55px;top:-22px">”</div>
    <p class="quote-text">Lorem Ipsum Is Simply Dummy Text Of The Printing And Typesetting Industry. Lorem Ipsum Has Been The Industry's Standard Dummy Text Ever Since The 1500s, When An Unknown Printer Took A Galley Of Type And Scrambled It To Make A Type Specimen Book. It Has Survived Not Only Five Centuries.</p>
    <div class="stars">★★★★★</div>
    <div class="who">Samir Haddad</div>
    <div class="role">Author Of Heritage Books</div>
  </div>
  <div class="abs dots"><i></i><i></i><i></i><i></i></div>
</section>

<section>
  <div class="abs cta-green"></div>
  <div class="abs cta-photo" role="img" aria-label="Downtown office towers beside a bridge"></div>
  <h2 class="abs cta-text serif">For All Your Construction Needs!</h2>
  <a class="abs btn-white cta-btn">Contact Us</a>
</section>

<footer>
  <div class="abs footer"></div>
  <div class="abs footer-shape" style="clip-path:polygon(60% 0,100% 10%,100% 100%,0 100%,0 40%,35% 30%)"></div>
  <div class="abs brand footer-brand"><span class="brand-mark"></span>KEYSTONE RIDGE</div>
  <div class="abs footer-divider"></div>
  <p class="abs footer-about">Keystone Ridge Construction, LLC Is A Veteran-Owned Business, And Is A Leading Force In The Construction Industry</p>
  <span class="abs follow">Follow Us:</span>
  <span class="abs social" style="left:891px" aria-label="Social link"></span>
  <span class="abs social on" style="left:939px" aria-label="Social link"></span>
  <span class="abs social" style="left:986px" aria-label="Social link"></span>
  <span class="abs social" style="left:1033px" aria-label="Social link"></span>
  <div class="abs bottom-bar"></div>
  <p class="abs copy">Copyright © 2024 KRC LLC Construction. All Right Reserved</p>
  <p class="abs legal"><span>Privacy Policy</span><span>Tearms &amp; Condition</span></p>
</footer>

</body>
</html>
```